Website for UK Fintech Company specialising in Auto-Finance asset management

We need a website for a FINTECH business called KELVO Asset Management. We have developed and licenced an innovative platform to provide financial institutions whom provide secured Asset finance loans to consumer and commercial clients, allowing for real time tracking and management of defaulted accounts pending repossession. The KELVO Asset Management platform is a total recoveries solution through the cycle, from the moment the lender has to recover the vehicle (due to default/non-payment) to the disposal of the vehicle (via sale at Motor Auctions or by selling to a Car dealership network). The data provided from external services allows the Financier to make informed decisions, such as whether it is economical to continue the recovery and decide which sales channel is better suited for their assets to maximise residual values and minimise financial losses. The KELVO platform provides an array of MI reporting and uses a systematic approach utilising exception reporting to identify key areas of non-performance to enable focus where needed. KELVO also provides a leading Debt collection service recovering end-of-cycle losses such as Financial Shortfall and losses in vehicle values due to conditions and excessive damage.

We also require a new logo for out new product called PL-Certify

Target Market(s)

Financial institutions whom provide secured Asset finance loans to consumer and commercial clients

Industry/Entity Type

Financial Service

Logo Text

PL- Certify (this is for a new product which forms part of the KELVO Asset Mangement Platform

Number of Pages Required

4 page

Font styles to use
Serif
Sans Serif

Colors

Designer to choose colors to be used in the design.

Requirements
Must have
• We need a simple website with a broken down as follows;
• • Landing page
• • Services page
• • About us page
• • KELVO Asset Management Platform login page (client facing)
Nice to have
• Our slogan is 'Auto-Finance Expertise'
• We are very much open to suggestions as long as we can create a professional/ corporate / modern feel to the website. We are a FINTECH company, and that needs to come across
Should not have
• Whilst we are an asset management company primarily managing vehicles through our platform, we don't want it to look like a car dealership website!:)

```html
<!DOCTYPE html>
<html lang="en">
<head>
<meta charset="utf-8">
<title>KELVO Asset Management Platform</title>
<link href="https://fonts.googleapis.com/css2?family=Roboto:wght@400;500;700&family=Open+Sans:ital,wght@0,400;0,600;1,400&display=swap" rel="stylesheet">
<style>
  :root {
    --orange: #f07c12;
    --orange-deep: #e86a0a;
    --orange-light: #f59a35;
    --dark: #2b2b2d;
    --ink: #1a1a1a;
    --body: #666666;
    --white: #ffffff;
    --footer: #d8d8d8;
    --footer-ink: #6a6a6a;
  }
  * { box-sizing: border-box; margin: 0; padding: 0; }
  html, body { width: 702px; height: 1200px; overflow: hidden; background: var(--white); }
  body { position: relative; font-family: "Open Sans", Arial, sans-serif; color: var(--body); }
  .abs { position: absolute; }

  /* Hero */
  .hero { position: absolute; left: 0; top: 0; width: 702px; height: 379px; overflow: hidden; }
  .hero-photo { position: absolute; inset: 0; background: linear-gradient(120deg, #3a3634 0%, #2c2a29 45%, #4a3d33 100%); }
  .hero-band { position: absolute; inset: 0; }
  .brand { position: absolute; left: 70px; top: 14px; }
  .brand-name { font-family: "Roboto", Arial, sans-serif; font-weight: 700; font-size: 34px; color: var(--white); letter-spacing: -0.5px; line-height: 1; display: flex; align-items: center; gap: 6px; }
  .brand-mark { width: 9px; height: 9px; background: var(--orange); display: inline-block; margin-top: -18px; }
  .brand-tag { font-family: "Roboto", Arial, sans-serif; font-weight: 500; font-size: 8.5px; color: var(--orange); margin-top: 4px; letter-spacing: 0.1px; }
  .nav { position: absolute; top: 28px; left: 262px; display: flex; gap: 23px; font-family: "Roboto", Arial, sans-serif; font-weight: 500; font-size: 10.5px; color: var(--white); }
  .nav .active { color: var(--orange); }
  .hero-title { position: absolute; left: 70px; top: 141px; font-family: "Roboto", Arial, sans-serif; font-weight: 500; font-size: 24px; line-height: 26px; color: var(--white); }
  .hero-text { position: absolute; left: 72px; top: 198px; width: 210px; font-size: 9.5px; line-height: 14.5px; color: var(--white); }
  .btn { position: absolute; width: 93px; height: 26px; border: 1.5px solid var(--orange); color: var(--orange); font-family: "Roboto", Arial, sans-serif; font-weight: 500; font-size: 9px; display: flex; align-items: center; justify-content: center; letter-spacing: 0.2px; }
  .btn-light { border-color: var(--white); color: var(--white); }
  .slider-arrow { position: absolute; width: 30px; height: 30px; border: 1.5px solid var(--white); border-radius: 50%; }
  .monitor { position: absolute; left: 366px; top: 114px; width: 259px; height: 204px; }

  /* About */
  .section-mark { position: absolute; width: 12px; height: 12px; background: var(--orange); left: 345px; }
  .section-title { position: absolute; left: 0; width: 702px; text-align: center; font-family: "Roboto", Arial, sans-serif; font-weight: 500; font-size: 19px; color: var(--ink); }
  .about-text { position: absolute; left: 116px; top: 461px; width: 470px; text-align: center; font-size: 9.4px; line-height: 14.5px; color: var(--body); }

  /* Why */
  .why { position: absolute; left: 0; top: 616px; width: 702px; height: 224px; background: linear-gradient(100deg, var(--orange-deep) 0%, var(--orange) 50%, var(--orange-light) 100%); }
  .why-title { position: absolute; left: 327px; top: 39px; font-family: "Roboto", Arial, sans-serif; font-weight: 500; font-size: 16.5px; color: var(--white); }
  .why-text { position: absolute; left: 330px; top: 66px; width: 318px; font-size: 8.9px; line-height: 15.6px; color: var(--white); }

  /* Testimonials */
  .card { position: absolute; top: 919px; width: 171px; height: 99px; background: var(--white); border-radius: 5px; box-shadow: 0 1px 8px rgba(0,0,0,0.13); }
  .card-quote { position: absolute; left: 13px; top: 12px; font-family: "Georgia", serif; font-size: 26px; line-height: 1; color: var(--orange); font-weight: 700; }
  .card-text { position: absolute; left: 33px; top: 22px; width: 128px; font-style: italic; font-size: 8.1px; line-height: 14.5px; color: var(--body); }
  .author { position: absolute; top: 1031px; display: flex; align-items: center; gap: 6px; }
  .avatar { width: 30px; height: 30px; border-radius: 50%; background: linear-gradient(135deg, #8a7a6a, #4f4a44); }
  .author-name { font-size: 8.8px; color: var(--ink); line-height: 12px; }
  .author-city { font-size: 7.6px; color: var(--body); line-height: 12px; }

  /* Footer */
  .footer { position: absolute; left: 0; top: 1106px; width: 702px; height: 94px; background: var(--footer); }
  .social { position: absolute; top: 22px; left: 303px; display: flex; gap: 4px; }
  .social span { width: 21px; height: 21px; border: 1.3px solid var(--ink); border-radius: 50%; display: block; }
  .copyright { position: absolute; top: 55px; width: 702px; text-align: center; font-size: 8.8px; color: var(--footer-ink); }
</style>
</head>
<body>

<header class="hero">
  <div class="hero-photo" role="img" aria-label="Photo of colleagues reviewing financial documents in an office"></div>
  <svg class="hero-band" width="702" height="379" viewBox="0 0 702 379" aria-hidden="true">
    <defs>
      <linearGradient id="bandFill" x1="0" y1="1" x2="1" y2="0">
        <stop offset="0" stop-color="#e8700c"/>
        <stop offset="1" stop-color="#f59a2a"/>
      </linearGradient>
    </defs>
    <polygon points="702,24 702,379 144,379" fill="url(#bandFill)"/>
  </svg>

  <div class="brand">
    <div class="brand-name">KELVO<span class="brand-mark"></span></div>
    <div class="brand-tag">ASSET MANAGEMENT PLATFORM</div>
  </div>

  <nav class="nav">
    <span class="active">HOME</span>
    <span>ABOUT US</span>
    <span>SERVICES</span>
    <span>WHY US</span>
    <span>SOLUTION</span>
    <span>CONTACT</span>
  </nav>

  <h1 class="hero-title">ASSET MANAGEMENT &amp;<br>SOLUTION SERVICES</h1>
  <p class="hero-text">We have developed and licenced an innovative platform to provide financial institutions</p>
  <div class="btn" style="left:72px;top:239px;">READ MORE</div>

  <svg class="slider-arrow" style="left:23px;top:172px;" viewBox="0 0 30 30" aria-label="Previous slide"><polyline points="17,9 11,15 17,21" fill="none" stroke="#fff" stroke-width="2.4"/></svg>
  <svg class="slider-arrow" style="left:650px;top:172px;" viewBox="0 0 30 30" aria-label="Next slide"><polyline points="13,9 19,15 13,21" fill="none" stroke="#fff" stroke-width="2.4"/></svg>

  <div class="monitor" role="img" aria-label="Desktop monitor showing the asset management platform dashboard" style="background:linear-gradient(180deg,#d9d9d9 0%,#bdbdbd 100%);border-radius:6px;"></div>
</header>

<section>
  <div class="section-mark" style="top:408px;"></div>
  <h2 class="section-title" style="top:429px;">ABOUT KELVO</h2>
  <p class="about-text">We have developed and licenced an innovative platform to provide financial institutions whom provide secured Asset finance loans to consumer and commercial clients, allowing for real time tracking and management of defaulted accounts pending repossession. The KELVO Asset Management platform is a total recoveries solution through the cycle, from the moment the lender has to recover the vehicle (due to default/non-payment) to the disposal of the vehicle (via sale at Motor Auctions or by selling to a Car dealership network).</p>
  <div class="btn" style="left:310px;top:548px;">READ MORE</div>
</section>

<section class="why" role="img" aria-label="Orange tinted photo of hands working on a laptop with financial reports">
  <h2 class="why-title">WHY WE ARE</h2>
  <p class="why-text">The KELVO platform provides an array of MI reporting and uses a systematic approach utilising exception reporting to identify key areas of non-performance to enable focus where needed. KELVO also provides a leading Debt collection service recovering end-of-cycle losses such as Financial Shortfall and losses in vehicle values due to conditions and excessive damag</p>
  <div class="btn btn-light" style="left:331px;top:158px;">READ MORE</div>
</section>

<section>
  <div class="section-mark" style="top:860px;"></div>
  <h2 class="section-title" style="top:880px;">TESTIMONIALS</h2>

  <div class="card" style="left:70px;"><span class="card-quote">&ldquo;</span><p class="card-text">Morbi diam mauris viverra in gravida eu mattis in ante Morbi eget arcu Morbi porta libero id ullamcorper nonummy nibh</p></div>
  <div class="card" style="left:266px;"><span class="card-quote">&ldquo;</span><p class="card-text">Morbi diam mauris viverra in gravida eu mattis in ante Morbi eget arcu Morbi porta libero id ullamcorper nonummy nibh</p></div>
  <div class="card" style="left:461px;"><span class="card-quote">&ldquo;</span><p class="card-text">Morbi diam mauris viverra in gravida eu mattis in ante Morbi eget arcu Morbi porta libero id ullamcorper nonummy nibh</p></div>

  <div class="author" style="left:75px;"><div class="avatar" role="img" aria-label="Author portrait"></div><div><div class="author-name">By Author Name</div><div class="author-city">City Location</div></div></div>
  <div class="author" style="left:271px;"><div class="avatar" role="img" aria-label="Author portrait"></div><div><div class="author-name">By Author Name</div><div class="author-city">City Location</div></div></div>
  <div class="author" style="left:466px;"><div class="avatar" role="img" aria-label="Author portrait"></div><div><div class="author-name">By Author Name</div><div class="author-city">City Location</div></div></div>
</section>

<footer class="footer">
  <div class="social" aria-label="Social links">
    <span aria-label="Social link"></span>
    <span aria-label="Social link"></span>
    <span aria-label="Social link"></span>
    <span aria-label="Social link"></span>
  </div>
  <p class="copyright">&copy; 2018 Company Name &nbsp;All right reserved &nbsp;Terms of Use</p>
</footer>

</body>
</html>
```